Real estate business needing a creative mind!

Have a real estate business called Brightlane Estates LLC. I need some business card with custom logo. That logo can be an intricate design of a house or houses. Maybe some blue and orange colors, maybe the business name in orange. Some thing that leaves a wow impression to the holder. Or just surprise me! Must have business name, name, email and phone number.

Target Market(s)

Property sellers and real estate professionals

Industry/Entity Type

Real estate

Contact Information for Business Card

Want it to stand out but also be professional.

Colors

Designer to choose colors to be used in the design.

Requirements
Must have
• Business name Brightlane Estates. My name which is Dale Venbrook. The business email which is Brightlaneestates1@mailpost.example. The phone number which is 555-604-1928
Nice to have
• Could be a logo of the name over some mountain houses being that we live by the Smokey mountains. Could have a sun if it looks ok?

```html
<!DOCTYPE html>
<html lang="en">
<head>
<meta charset="utf-8">
<title>Brightlane Estates LLC – Business Card</title>
<link rel="stylesheet" href="https://fonts.googleapis.com/css2?family=Montserrat:wght@400;500;800&display=swap">
<style>
  :root {
    --navy: #06264f;
    --navy-deep: #03214a;
    --orange: #f08a24;
    --ink: #1d1d1f;
    --paper: #ffffff;
    --backdrop: #e9eaec;
  }
  * { margin: 0; padding: 0; box-sizing: border-box; }
  html, body { width: 1200px; height: 1200px; overflow: hidden; }
  body {
    background: var(--backdrop);
    font-family: "Montserrat", sans-serif;
    position: relative;
  }
  .card {
    position: absolute;
    left: 180px;
    width: 840px;
    height: 480px;
    border-radius: 36px;
    overflow: hidden;
    box-shadow: 0 10px 30px rgba(0,0,0,0.18);
  }
  .card--front { top: 90px; background: var(--paper); }
  .card--back { top: 630px; background: var(--navy-deep); }

  .band { position: absolute; bottom: 0; }
  .band--orange { left: 0; width: 64%; height: 56px; background: var(--orange); }
  .band--navy { right: 0; width: 34.5%; height: 150px; background: var(--navy); }

  .contact { position: absolute; left: 70px; top: 170px; color: var(--ink); }
  .contact__name {
    font-weight: 800; font-size: 44px; color: var(--navy);
    letter-spacing: 1px; line-height: 1;
  }
  .contact__title {
    font-weight: 500; font-size: 22px; letter-spacing: 1px;
    margin-top: 8px; text-transform: uppercase;
  }
  .contact__list { list-style: none; margin-top: 24px; }
  .contact__item {
    display: flex; align-items: center; gap: 14px;
    font-size: 19px; font-weight: 500; margin-bottom: 10px;
  }
  .contact__icon { width: 22px; height: 22px; fill: var(--navy); flex: none; }

  .brand {
    position: absolute; display: flex; align-items: center;
    font-weight: 800; letter-spacing: 1px; text-transform: uppercase;
  }
  .brand__dot { border-radius: 50%; background: var(--orange); flex: none; }
  .brand--front {
    right: 50px; top: 110px; width: 330px; gap: 16px;
    color: var(--navy); font-size: 28px; line-height: 1.15;
  }
  .brand--front .brand__dot { width: 56px; height: 56px; }
  .brand--back {
    left: 0; right: 0; top: 0; bottom: 0; justify-content: center; gap: 26px;
    color: var(--paper); font-size: 46px; line-height: 1.15;
  }
  .brand--back .brand__dot { width: 96px; height: 96px; }
</style>
</head>
<body>
  <section class="card card--front">
    <div class="brand brand--front">
      <span class="brand__dot"></span>
      <span class="brand__name">Brightlane Estates LLC</span>
    </div>

    <div class="contact">
      <h1 class="contact__name">DALE VENBROOK</h1>
      <p class="contact__title">Real Estate Agent</p>
      <ul class="contact__list">
        <li class="contact__item">
          <svg class="contact__icon" viewBox="0 0 24 24" aria-hidden="true"><path d="M6.6 10.8a15.1 15.1 0 0 0 6.6 6.6l2.2-2.2a1 1 0 0 1 1-.25 11.4 11.4 0 0 0 3.6.57 1 1 0 0 1 1 1V20a1 1 0 0 1-1 1A17 17 0 0 1 3 4a1 1 0 0 1 1-1h3.5a1 1 0 0 1 1 1c0 1.25.2 2.45.57 3.57a1 1 0 0 1-.25 1z"/></svg>
          <span>555-604-1928</span>
        </li>
        <li class="contact__item">
          <svg class="contact__icon" viewBox="0 0 24 24" aria-hidden="true"><path d="M2 5h20v14H2z M3.5 6.5 12 13l8.5-6.5" fill="none" stroke="#06264f" stroke-width="2"/><path d="M2 5h20L12 12.5z"/></svg>
          <span>brightlaneestates1@mailpost.example</span>
        </li>
      </ul>
    </div>

    <div class="band band--orange"></div>
    <div class="band band--navy"></div>
  </section>

  <section class="card card--back">
    <div class="brand brand--back">
      <span class="brand__dot"></span>
      <span class="brand__name">Brightlane<br>Estates LLC</span>
    </div>
  </section>
</body>
</html>
```